Pellmore Heating & Air

I need a business card made for my company. I would like my new logo for Pellmore Heating and Air on the front and my Garage Door on the back.
Front to say -Heating & Air Conditioning , Mini Splits and Heat Pumps, Hydronic In-Floor Heat. Locally Owned and Operated! Licensed, Boned and Insured. Free Estimates on new equipment. 555-201-4837
KVB Back Card, change phone# to 555-318-6024. Remove Commercial and residential and fully sticked vans lines.

```html
<!DOCTYPE html>
<html lang="en">
<head>
<meta charset="utf-8">
<title>Pellmore Heating &amp; Air / Kinvale Garage Door – Business Cards</title>
<link rel="stylesheet" href="https://fonts.googleapis.com/css2?family=Open+Sans:wght@400;600;700;800&family=Russo+One&display=swap">
<style>
  :root {
    --bg: #232323;
    --card: #1d1e21;
    --card-deep: #161719;
    --card-mid: #1a1b1e;
    --red: #ec1c24;
    --blue: #1b5ea3;
    --white: #ffffff;
    --muted: #e8e8e8;
  }
  * { box-sizing: border-box; margin: 0; padding: 0; }
  html, body {
    width: 1200px; height: 780px; overflow: hidden;
    background: var(--bg);
    font-family: "Open Sans", Arial, sans-serif;
    color: var(--white);
  }
  .canvas {
    position: relative; width: 1200px; height: 780px;
    display: flex; justify-content: center; align-items: center; gap: 90px;
  }
  .card {
    position: relative; width: 320px; height: 560px;
    background: var(--card);
    border-radius: 26px; overflow: hidden;
    box-shadow: 0 18px 40px rgba(0,0,0,.55);
  }
  .card-bands { position: absolute; inset: 0; width: 100%; height: 100%; }
  .card-content {
    position: relative; height: 100%;
    display: flex; flex-direction: column; align-items: center;
    text-align: center; padding: 44px 20px 0;
  }
  .brand {
    display: flex; align-items: center; gap: 10px;
    font-weight: 800; font-size: 26px; line-height: 1.05;
    color: var(--red); letter-spacing: .3px;
  }
  .brand-dot { width: 16px; height: 16px; border-radius: 50%; background: var(--blue); flex: none; }
  .brand-name { text-align: left; }
  .save-card {
    margin-top: 30px;
    font-family: "Russo One", Arial, sans-serif;
    font-size: 25px; color: var(--red); letter-spacing: 1px;
  }
  .phone { font-weight: 700; font-size: 27px; line-height: 1.15; margin-top: 2px; }
  .email { font-size: 13px; font-weight: 600; margin-top: 3px; color: var(--muted); }
  .services {
    list-style: none; margin-top: 22px;
    font-size: 13.5px; font-weight: 600; line-height: 1.4;
  }
  .services li::before { content: "• "; }
  .offer { position: relative; width: 240px; height: 98px; margin-top: 14px; }
  .offer svg { position: absolute; inset: 0; width: 100%; height: 100%; }
  .offer-text {
    position: relative; height: 100%;
    display: flex; flex-direction: column; justify-content: center; align-items: center;
    line-height: 1.05;
  }
  .offer-free { font-family: "Russo One", Arial, sans-serif; font-size: 27px; letter-spacing: 1px; }
  .offer-detail { font-size: 13px; font-weight: 700; }
  .website {
    position: absolute; left: 0; right: 0; bottom: 38px; text-align: center;
  }
  .website-label { font-size: 15px; font-weight: 600; }
  .website-url { font-size: 17px; font-weight: 600; }
  .website-url strong { font-size: 25px; font-weight: 600; }
  .card--garage .services { margin-top: 34px; font-size: 14px; }
  .card--garage .offer { margin-top: 30px; }
  .card--garage .offer-detail { font-size: 15px; letter-spacing: .3px; }
</style>
</head>
<body>
<main class="canvas">

  <!-- Front: heating & air -->
  <article class="card card--heating">
    <svg class="card-bands" viewBox="0 0 320 560" preserveAspectRatio="none" aria-hidden="true">
      <rect width="320" height="560" fill="var(--card-deep)"/>
      <path d="M0 0 H320 V340 C300 440 200 500 0 500 Z" fill="var(--card-mid)"/>
      <path d="M0 0 H320 V300 C290 400 190 440 70 440 H0 Z" fill="var(--card)"/>
    </svg>
    <div class="card-content">
      <div class="brand"><span class="brand-dot"></span><span class="brand-name">Pellmore<br>Heating &amp; Air</span></div>
      <p class="save-card">SAVE THIS CARD!</p>
      <p class="phone">555-201-4837</p>
      <p class="email">kinvalegaragedoor@example.com</p>
      <ul class="services">
        <li>Boned and Insured</li>
        <li>Hydronic In-Floor Heat</li>
        <li>Heating &amp; Air Conditioning</li>
        <li>Mini Splits and Heat Pumps</li>
        <li>Locally Owned and Operated! Licensed</li>
      </ul>
      <div class="offer">
        <svg viewBox="0 0 270 110" preserveAspectRatio="none" aria-hidden="true">
          <polygon fill="var(--red)" stroke="var(--blue)" stroke-width="1.5" points="265,55 231.6,63.8 247.6,80 205.7,79 200,98.3 160.9,87.8 135,105 109.1,87.8 70,98.3 64.3,79 22.4,80 38.4,63.8 5,55 38.4,46.2 22.4,30 64.3,31 70,11.7 109.1,22.2 135,5 160.9,22.2 200,11.7 205.7,31 247.6,30 231.6,46.2"/>
        </svg>
        <div class="offer-text">
          <span class="offer-free">FREE</span>
          <span class="offer-detail">Estimates on<br>new equipment</span>
        </div>
      </div>
    </div>
    <div class="website">
      <p class="website-label">Visit Our Website:</p>
      <p class="website-url">www.<strong>KinvaleGarage</strong> Door.com</p>
    </div>
  </article>

  <!-- Back: garage door -->
  <article class="card card--garage">
    <svg class="card-bands" viewBox="0 0 320 560" preserveAspectRatio="none" aria-hidden="true">
      <rect width="320" height="560" fill="var(--card-deep)"/>
      <path d="M0 0 H320 V330 C300 430 200 480 0 485 Z" fill="var(--card-mid)"/>
      <path d="M0 0 H320 V290 C290 390 190 425 70 425 H0 Z" fill="var(--card)"/>
    </svg>
    <div class="card-content">
      <div class="brand"><span class="brand-dot"></span><span class="brand-name">Kinvale<br>Garage Door</span></div>
      <p class="save-card">SAVE THIS CARD!</p>
      <p class="phone">555-318-6024</p>
      <p class="email">kinvalegaragedoor@example.com</p>
      <ul class="services">
        <li>Same Day &amp; Emergency Service</li>
        <li>Locally Owned &amp; Operated</li>
        <li>All Major Brands</li>
      </ul>
      <div class="offer">
        <svg viewBox="0 0 270 110" preserveAspectRatio="none" aria-hidden="true">
          <polygon fill="var(--red)" stroke="var(--blue)" stroke-width="1.5" points="265,55 231.6,63.8 247.6,80 205.7,79 200,98.3 160.9,87.8 135,105 109.1,87.8 70,98.3 64.3,79 22.4,80 38.4,63.8 5,55 38.4,46.2 22.4,30 64.3,31 70,11.7 109.1,22.2 135,5 160.9,22.2 200,11.7 205.7,31 247.6,30 231.6,46.2"/>
        </svg>
        <div class="offer-text">
          <span class="offer-free">FREE</span>
          <span class="offer-detail">SERVICE CALL</span>
        </div>
      </div>
    </div>
    <div class="website">
      <p class="website-label">Visit Our Website:</p>
      <p class="website-url">www.<strong>KinvaleGarage</strong> Door.com</p>
    </div>
  </article>

</main>
</body>
</html>
```